NEW Business Cards!
CNC Machine Shop Business Cards
Simple
Dale Workman
248 North Route 371
Kelvale, Texas 75418
WorkmanIronCraft@mailbox-example.com
www.WorkmanIronCraft.example
We also need this person on the same card somehow:
Travis Workman
Cell - 555.218.7730
Fax - Same
email - Same
In-House Services:
CNC Milling
CNC Turning
CNC Bending
Water Jet Cutting
Powder Coating

```html
<!DOCTYPE html>
<html lang="en">
<head>
<meta charset="utf-8">
<title>Workman Iron Craft – Business Cards</title>
<link rel="stylesheet" href="https://fonts.googleapis.com/css2?family=Arimo:wght@400;700&display=swap">
<style>
  :root {
    --backdrop: #e9e6e1;
    --card-white: #ffffff;
    --gold-dark: #7a5a22;
    --gold-mid: #c7a15c;
    --gold-light: #f1dca6;
    --steel-blue: #1f5fa8;
    --ink: #2b2b2b;
    --ink-soft: #555555;
    --rule: #9a9a9a;
  }
  * { box-sizing: border-box; margin: 0; padding: 0; }
  html, body { width: 1200px; height: 886px; overflow: hidden; }
  body {
    background: var(--backdrop);
    font-family: "Arimo", Arial, sans-serif;
    position: relative;
  }
  .card {
    position: absolute;
    top: 269px;
    width: 245px;
    height: 410px;
    box-shadow: 0 4px 14px rgba(0,0,0,.25);
    overflow: hidden;
  }
  .card--contact { left: 187px; background: var(--card-white); }
  .card--gold {
    left: 468px;
    background: linear-gradient(90deg, var(--gold-dark) 0%, var(--gold-mid) 30%, var(--gold-light) 50%, var(--gold-mid) 70%, var(--gold-dark) 100%);
  }
  .card--white { left: 744px; background: var(--card-white); }

  .name-band {
    height: 84px;
    padding: 10px 14px;
    background: linear-gradient(90deg, var(--gold-dark), var(--gold-mid) 45%, var(--gold-light) 60%, var(--gold-mid) 80%, var(--gold-dark));
    color: #fff;
  }
  .person { font-weight: 700; font-size: 15px; line-height: 17px; }
  .person-cell { font-size: 9px; line-height: 12px; margin-bottom: 4px; }

  .brand {
    display: flex;
    align-items: center;
    justify-content: center;
    gap: 8px;
    color: var(--steel-blue);
    font-weight: 700;
    text-align: center;
  }
  .brand-square { width: 14px; height: 14px; background: var(--steel-blue); flex: none; }
  .card--contact .brand { margin-top: 52px; font-size: 22px; line-height: 24px; }
  .card--gold .brand, .card--white .brand { margin-top: 62px; font-size: 24px; line-height: 26px; }
  .card--gold .brand { color: #183f73; }
  .card--gold .brand-square { background: #183f73; }

  .contact-block {
    position: absolute;
    left: 28px;
    top: 310px;
    padding-left: 8px;
    border-left: 1px solid var(--rule);
    font-size: 8.5px;
    line-height: 11px;
    color: var(--ink-soft);
  }
  .contact-gap { height: 16px; }

  .services {
    position: absolute;
    left: 40px;
    top: 242px;
    color: var(--ink);
    font-size: 14px;
    line-height: 16.5px;
  }
  .services h2 { font-size: 14px; font-weight: 400; margin-bottom: 1px; }
  .services ul { list-style: none; padding-left: 4px; }
  .services li { display: flex; align-items: center; gap: 6px; }
  .services svg { flex: none; }
</style>
</head>
<body>

<section class="card card--contact">
  <div class="name-band">
    <p class="person">Dale Workman</p>
    <p class="person-cell">Cell: 555.304.6129</p>
    <p class="person">Travis Workman</p>
    <p class="person-cell">Cell: 555.218.7730</p>
  </div>
  <div class="brand">
    <span class="brand-square"></span>
    <span>WORKMAN<br>IRON CRAFT</span>
  </div>
  <div class="contact-block">
    <p>248 North Route 371</p>
    <p>Kelvale, Texas 75418</p>
    <div class="contact-gap"></div>
    <p>Email: WorkmanIronCraft@mailbox-example.com</p>
    <p>Web: www.WorkmanIronCraft.example</p>
  </div>
</section>

<section class="card card--gold">
  <div class="brand">
    <span class="brand-square"></span>
    <span>WORKMAN</span>
  </div>
  <div class="services">
    <h2>In-House Services:</h2>
    <ul>
      <li><svg width="12" height="8" viewBox="0 0 12 8"><path d="M6 0 12 4 6 8 0 4Z" fill="#1f5fa8"/></svg>CNC Milling</li>
      <li><svg width="12" height="8" viewBox="0 0 12 8"><path d="M6 0 12 4 6 8 0 4Z" fill="#1f5fa8"/></svg>CNC Turning</li>
      <li><svg width="12" height="8" viewBox="0 0 12 8"><path d="M6 0 12 4 6 8 0 4Z" fill="#1f5fa8"/></svg>CNC Bending</li>
      <li><svg width="12" height="8" viewBox="0 0 12 8"><path d="M6 0 12 4 6 8 0 4Z" fill="#1f5fa8"/></svg>Water Jet Cutting</li>
      <li><svg width="12" height="8" viewBox="0 0 12 8"><path d="M6 0 12 4 6 8 0 4Z" fill="#1f5fa8"/></svg>Powder Coating</li>
    </ul>
  </div>
</section>

<section class="card card--white">
  <div class="brand">
    <span class="brand-square"></span>
    <span>WORKMAN</span>
  </div>
  <div class="services">
    <h2>In-House Services:</h2>
    <ul>
      <li><svg width="12" height="8" viewBox="0 0 12 8"><path d="M6 0 12 4 6 8 0 4Z" fill="#1f5fa8"/></svg>CNC Milling</li>
      <li><svg width="12" height="8" viewBox="0 0 12 8"><path d="M6 0 12 4 6 8 0 4Z" fill="#1f5fa8"/></svg>CNC Turning</li>
      <li><svg width="12" height="8" viewBox="0 0 12 8"><path d="M6 0 12 4 6 8 0 4Z" fill="#1f5fa8"/></svg>Forming</li>
      <li><svg width="12" height="8" viewBox="0 0 12 8"><path d="M6 0 12 4 6 8 0 4Z" fill="#1f5fa8"/></svg>Water Jet Cutting</li>
      <li><svg width="12" height="8" viewBox="0 0 12 8"><path d="M6 0 12 4 6 8 0 4Z" fill="#1f5fa8"/></svg>Powder Coating</li>
    </ul>
  </div>
</section>

</body>
</html>
```